Wendale Ridge Concrete Pumping needs a logo design and is in the concrete industry

A creative design for this Wendale Ridge Concrete Pumping business. Using a trailer mounted line pump, not a boom pump.
Colour to be used is orange and a mix of white or black writing.
Target Market(s)
General Public, anyone
Industry/Entity Type
Concrete
Contact Information for Business Card
Wendale Ridge Concrete Pumping
Callum Hesketh
PO BOX 47
Merrowbank VIC 3318
Phone: 0417952803
Email: Hesketh@bluewrenmail.com.au
Colors
f37122
000000
ffffff
Requirements
Must have
- Details listed
Nice to have
- A great logo
Should not have
- anything silly

```html
<!DOCTYPE html>
<html lang="en">
<head>
<meta charset="utf-8">
<title>Wendale Ridge Concrete Pumping – Business Card</title>
<link rel="stylesheet" href="https://fonts.googleapis.com/css2?family=Lato:wght@400;700;900&display=swap">
<style>
  :root {
    --orange: #e0622a;
    --orange-band: #d9663a;
    --ink: #1a1a1a;
    --text: #2a2a2a;
    --card: #efedea;
    --card-edge: #d8d4cf;
    --page: #d6d1ca;
  }
  html, body {
    margin: 0;
    padding: 0;
    width: 970px;
    height: 1200px;
    overflow: hidden;
    background: var(--page);
    font-family: "Lato", sans-serif;
  }
  .card {
    position: absolute;
    left: 175px;
    top: 60px;
    width: 620px;
    height: 1080px;
    border-radius: 30px;
    background: linear-gradient(180deg, #f3f2f0 0%, var(--card) 55%, #e9e6e2 100%);
    border: 1px solid var(--card-edge);
    box-shadow: 0 8px 30px rgba(0,0,0,0.12);
    overflow: hidden;
    color: var(--text);
    text-align: center;
  }
  .brand {
    position: absolute;
    left: 0;
    right: 0;
    top: 120px;
  }
  .brand-mark {
    display: block;
    width: 54px;
    height: 54px;
    margin: 0 auto 26px;
    background: var(--orange);
  }
  .brand-name {
    margin: 0;
    font-weight: 900;
    font-size: 44px;
    line-height: 1.15;
    letter-spacing: 0.5px;
    color: var(--orange);
    text-transform: uppercase;
  }
  .person {
    position: absolute;
    left: 0;
    right: 0;
    top: 492px;
  }
  .person-name {
    margin: 0;
    font-weight: 900;
    font-size: 38px;
    line-height: 1;
    color: var(--ink);
  }
  .person-role {
    margin: 4px 0 0;
    font-size: 30px;
    line-height: 1.1;
    color: var(--orange);
  }
  .contact {
    position: absolute;
    left: 0;
    right: 0;
    top: 648px;
    margin: 0;
  }
  .contact dt {
    font-size: 24px;
    line-height: 1;
    color: var(--orange);
    text-transform: uppercase;
  }
  .contact dd {
    margin: 14px 0 30px;
    font-size: 32px;
    line-height: 1;
    color: var(--text);
  }
  .contact dd.address {
    font-size: 34px;
    margin-bottom: 0;
  }
  .rule {
    position: absolute;
    left: 0;
    right: 0;
    top: 986px;
    height: 3px;
    background: #2b2b2b;
  }
  .band {
    position: absolute;
    left: 0;
    right: 0;
    top: 998px;
    bottom: 0;
    background: var(--orange-band);
  }
</style>
</head>
<body>
  <div class="card">
    <header class="brand">
      <span class="brand-mark"></span>
      <h1 class="brand-name">Wendale Ridge<br>Concrete Pumping</h1>
    </header>

    <section class="person">
      <h2 class="person-name">CALLUM HESKETH</h2>
      <p class="person-role">Director</p>
    </section>

    <dl class="contact">
      <dt>Phone</dt>
      <dd>0417952803</dd>
      <dt>Email</dt>
      <dd>Hesketh@bluewrenmail.com.au</dd>
      <dt>Address</dt>
      <dd class="address">PO BOX 47, Merrowbank VIC 3318</dd>
    </dl>

    <div class="rule"></div>
    <div class="band"></div>
  </div>
</body>
</html>
```